Windshield wiper website

I have a website through hostravel.com named NQBclearo.com
I'm looking to include the windshield wiper sizes needed for vehicles in a user-friendly format. Along with a page to order the wipers from. I supply all the wiper blades in sizes 14,16,17,18,19,20,21,22,24,26,28,30, and 32"
The wiper blades are silicone beam blade.
Our motto is 'see it clearly'
I've tried designing a website already at nqbclearo.com but I feel like it doesn't look legit enough to acquire sales.

Target Market(s)

Every vehicle in the USA.

Industry/Entity Type

Auto parts - New

Coding

Coded - Design and coding required

Number of Pages Required

5+ page

Font styles to use
Sans Serif

Requirements
Must have
• User friendly way to find out what size windshield wiper they need for their specific vehicle.
Nice to have
• A way to automatically email a purchaser one year after a sale to get a repeat customer.

```html
<!DOCTYPE html>
<html lang="en">
<head>
<meta charset="utf-8">
<title>NQB Clearo — See It Clearly</title>
<link href="https://fonts.googleapis.com/css2?family=Jost:wght@400;500;600;700&family=Nunito+Sans:wght@400;600;700&display=swap" rel="stylesheet">
<style>
:root{
  --gold:#b5975a;
  --gold-light:#d9c48f;
  --gold-dark:#8f7440;
  --ink:#161616;
  --white:#ffffff;
  --stage:#c8c8c8;
  --text:#2a2a2a;
}
*{box-sizing:border-box;margin:0;padding:0}
html,body{width:1200px;height:4232px;overflow:hidden}
body{background:var(--stage);font-family:"Nunito Sans",sans-serif;color:var(--text)}
.page{position:absolute;left:0;top:390px;width:1200px;height:3452px;background:var(--white);overflow:hidden}
.abs{position:absolute}
.gold{color:var(--gold)}

/* header */
.site-header{left:0;top:0;width:1200px;height:168px;background:var(--ink)}
.contact-strip{left:419px;top:4px;width:781px;height:50px;border-radius:25px 0 0 25px;background:linear-gradient(90deg,var(--gold-light),var(--gold));display:flex;align-items:center;padding-left:38px;gap:10px;font-size:15px;color:var(--ink)}
.contact-strip b{font-weight:700}
.strip-social{display:flex;gap:8px;margin-left:24px}
.strip-social span{width:24px;height:24px;border-radius:50%;background:var(--ink)}
.brand{display:flex;align-items:center;gap:12px;font-family:"Jost",sans-serif}
.brand-dot{width:34px;height:34px;border-radius:50%;background:var(--gold);flex:none}
.brand-name{color:var(--gold);font-weight:600;font-size:28px;white-space:nowrap}
.header-brand{left:90px;top:78px}
.main-nav{left:415px;top:98px;font-family:"Jost",sans-serif;color:var(--white);font-size:17px}
.main-nav a{color:inherit;text-decoration:none;position:absolute;white-space:nowrap}
.header-tools{left:960px;top:96px;display:flex;gap:22px;align-items:center}
.header-tools .sep{width:1px;height:18px;background:var(--gold-dark)}

/* hero */
.hero{left:0;top:168px;width:1200px;height:649px}
.hero-copy{left:100px;top:330px;color:var(--white);font-family:"Jost",sans-serif}
.hero-welcome{font-size:26px;font-weight:500}
.hero-title{font-size:62px;font-weight:700;line-height:1.05;margin-top:6px}
.btn{display:inline-flex;align-items:center;gap:14px;height:40px;padding:0 12px 0 20px;border-radius:20px;background:linear-gradient(90deg,var(--gold),var(--gold-light));color:var(--white);font-family:"Jost",sans-serif;font-weight:600;font-size:16px;letter-spacing:.5px}
.btn .arrow{width:20px;height:20px;border-radius:50%;background:var(--white);display:flex;align-items:center;justify-content:center}
.hero-dots{left:100px;top:648px;display:flex;gap:14px}
.hero-dots span{width:10px;height:10px;border-radius:50%;border:1.5px solid var(--white)}
.hero-dots span.on{background:var(--gold);border-color:var(--gold)}

/* about */
.about-photo{left:100px;top:872px}
.about-copy{left:600px;top:893px;width:500px}
.about-copy h2{font-family:"Jost",sans-serif;font-weight:600;font-size:31px;line-height:1.2;color:var(--ink)}
.about-copy h3{font-family:"Jost",sans-serif;font-weight:600;font-size:31px;color:var(--gold);line-height:1.2}
.about-copy p{font-size:14.5px;line-height:1.35;margin-top:20px;color:var(--text)}

/* products */
.products{left:0;top:1340px;width:1200px;height:776px}
.products-head{left:0;top:1500px;width:1200px;display:flex;flex-direction:column;align-items:center;color:var(--white)}
.products-head h2{font-family:"Jost",sans-serif;font-weight:600;font-size:34px;letter-spacing:.5px}
.products-head p{font-size:17px;margin-top:8px}
.product{width:227px;text-align:center;color:var(--white);font-family:"Jost",sans-serif}
.product-photo{width:227px;height:283px;border:3px solid var(--gold-light);background:linear-gradient(180deg,#dedede 0%,#b9b9b9 55%,#e9e9e9 100%);position:relative}
.quick-view{position:absolute;left:10px;bottom:12px;width:200px;height:36px;background:rgba(0,0,0,.85);color:var(--white);font-size:14px;text-align:left;padding:9px 12px}
.product-name{font-weight:600;font-size:15px;margin-top:22px}
.product-size{font-size:14px;margin-top:6px}
.product-price{color:var(--gold);font-weight:600;font-size:16px;margin-top:12px}
.stars{color:var(--gold);font-size:15px;letter-spacing:2px;margin-top:8px}
.stars .off{color:var(--white)}
.carousel-arrow{color:var(--white);font-size:34px;font-family:"Jost",sans-serif}

/* facts */
.fact{width:319px;height:238px;border-radius:4px;padding:62px 26px 0;text-align:center;color:var(--white);background:linear-gradient(180deg,#3a3a3a,#0c0c0c)}
.fact.highlight{background:linear-gradient(180deg,var(--gold),var(--gold-light))}
.fact h4{font-family:"Jost",sans-serif;font-weight:500;font-size:17px}
.fact p{font-size:11.5px;line-height:1.35;margin-top:14px}
.fact-icon{width:104px;height:104px;border-radius:50%;background:var(--white);border:4px solid var(--gold);display:flex;align-items:center;justify-content:center}

/* signup */
.signup-bg{left:0;top:2656px;width:1200px;height:600px;background:linear-gradient(180deg,#262626,#151515)}
.signup{left:102px;top:2527px;width:1002px;height:293px;border-radius:40px;background:linear-gradient(90deg,var(--gold-dark),var(--gold) 50%,var(--gold-dark));overflow:hidden;text-align:center;color:var(--white)}
.signup h2{font-family:"Jost",sans-serif;font-weight:600;font-size:40px;margin-top:42px;letter-spacing:.5px}
.divider{width:170px;height:2px;background:var(--white);margin:12px auto 0}
.signup p{font-size:16px;margin-top:14px}
.signup-form{position:absolute;left:211px;top:186px;width:582px;height:46px;background:var(--white);border-radius:4px 8px 8px 4px;display:flex;align-items:center}
.signup-form span{flex:1;text-align:left;padding-left:16px;color:var(--ink);font-size:16px}
.signup-form b{width:144px;height:46px;border-radius:8px;background:var(--ink);color:var(--gold);font-family:"Jost",sans-serif;font-weight:500;font-size:17px;display:flex;align-items:center;justify-content:center}

/* footer */
.footer-brand{left:0;top:2920px;width:1200px;justify-content:center}
.footer-card{width:265px;height:183px;border:1.5px solid #8a8a8a;background:#0f0f0f;text-align:center;color:var(--white);padding-top:22px}
.footer-icon{width:62px;height:62px;border-radius:50%;background:var(--gold);margin:0 auto;display:flex;align-items:center;justify-content:center}
.footer-card h5{color:var(--gold);font-family:"Jost",sans-serif;font-weight:600;font-size:17px;margin-top:18px}
.footer-card p{font-size:14px;margin-top:4px;line-height:1.3}
.footer-bar{left:0;top:3250px;width:1200px;height:202px;background:linear-gradient(90deg,var(--gold-dark),var(--gold-light) 40%,var(--gold) 70%,var(--gold-dark))}
.footer-social{left:0;top:3276px;width:1200px;display:flex;justify-content:center;gap:12px}
.footer-social span{width:34px;height:34px;border-radius:50%;background:var(--ink)}
.footer-links{left:0;top:3343px;width:1200px;display:flex;justify-content:center;gap:52px;font-family:"Jost",sans-serif;font-size:16px;color:var(--ink)}
.footer-copy{left:0;top:3403px;width:1200px;text-align:center;font-size:12px;letter-spacing:1.5px;color:var(--ink)}
</style>
</head>
<body>
<main class="page">

  <header class="abs site-header">
    <div class="abs contact-strip">
      <svg width="22" height="22" viewBox="0 0 22 22"><circle cx="11" cy="11" r="11" fill="#161616"/><path d="M7 6c1-1 2 0 2.5 1.2l.6 1.3c.2.6-.4 1-.8 1.4.7 1.4 1.6 2.3 3 3 .4-.4.8-1 1.4-.8l1.3.6c1.2.5 2.2 1.5 1.2 2.5-1.8 1.8-5 0-7-2S5.2 7.8 7 6z" fill="#d9c48f"/></svg>
      <span><b>Call us:</b> (123) 456-7890 |</span>
      <svg width="22" height="22" viewBox="0 0 22 22"><circle cx="11" cy="11" r="11" fill="#161616"/><rect x="6" y="7.5" width="10" height="7" rx="1" fill="#d9c48f"/><path d="M6 8l5 4 5-4" stroke="#161616" fill="none"/></svg>
      <span><b>Email us:</b> info@nqbclearo.com</span>
      <div class="strip-social"><span></span><span></span><span></span></div>
    </div>
    <div class="abs brand header-brand">
      <span class="brand-dot"></span>
      <span class="brand-name">NQB Clearo</span>
    </div>
    <nav class="abs main-nav">
      <a style="left:0">Home</a>
      <a style="left:106px">About Us</a>
      <a style="left:238px">Product</a>
      <a style="left:361px">Contact us</a>
    </nav>
    <div class="abs header-tools">
      <svg width="22" height="22" viewBox="0 0 22 22" fill="none" stroke="#b5975a" stroke-width="2"><circle cx="9" cy="9" r="6.5"/><path d="M14 14l6 6"/></svg>
      <span class="sep"></span>
      <svg width="24" height="24" viewBox="0 0 24 24" fill="none" stroke="#b5975a" stroke-width="1.8"><circle cx="12" cy="12" r="10.5"/><circle cx="12" cy="10" r="3.5"/><path d="M5.5 19c1.5-3 4-4 6.5-4s5 1 6.5 4"/></svg>
      <span class="sep"></span>
      <svg width="20" height="24" viewBox="0 0 20 24" fill="none" stroke="#b5975a" stroke-width="1.8"><rect x="2" y="8" width="16" height="14" rx="1.5"/><path d="M6 8V6a4 4 0 018 0v2"/></svg>
    </div>
  </header>

  <section class="abs hero">
    <svg width="1200" height="649" viewBox="0 0 1200 649">
      <defs>
        <linearGradient id="heroPhoto" x1="0" y1="0" x2="1" y2="1">
          <stop offset="0" stop-color="#5c6064"/><stop offset=".45" stop-color="#2f3336"/><stop offset=".75" stop-color="#3b4047"/><stop offset="1" stop-color="#1d2024"/>
        </linearGradient>
        <linearGradient id="goldArc" x1="0" y1="0" x2="1" y2="0">
          <stop offset="0" stop-color="#d9c48f"/><stop offset=".5" stop-color="#b5975a"/><stop offset="1" stop-color="#e3d09e"/>
        </linearGradient>
      </defs>
      <path d="M0 494 C260 610 480 660 720 636 C960 612 1130 470 1200 283 V330 C1130 510 960 640 720 650 C470 662 250 620 0 510 Z" fill="url(#goldArc)"/>
      <path role="img" aria-label="Photo of a hand in a blue sleeve fitting a wiper blade onto a wet windshield" d="M0 0 H1200 V283 C1130 470 960 600 720 620 C480 640 260 600 0 494 Z" fill="url(#heroPhoto)"/>
    </svg>
  </section>
  <div class="abs hero-copy">
    <div class="hero-welcome">Welcome to</div>
    <div class="hero-title"><span class="gold">NQB CLEARO</span><br>SEE IT CLEARLY</div>
    <div class="btn" style="margin-top:18px">LEARN MORE <span class="arrow"><svg width="12" height="12" viewBox="0 0 12 12"><path d="M2 6h7M6 3l3 3-3 3" stroke="#b5975a" stroke-width="1.8" fill="none"/></svg></span></div>
  </div>
  <div class="abs hero-dots"><span class="on"></span><span></span><span></span><span></span></div>

  <div class="abs about-photo">
    <svg width="450" height="440" viewBox="0 0 450 440">
      <defs><linearGradient id="aboutPhoto" x1="0" y1="0" x2="1" y2="1"><stop offset="0" stop-color="#4a6fa8"/><stop offset=".5" stop-color="#8d8b8e"/><stop offset="1" stop-color="#5d5558"/></linearGradient></defs>
      <path d="M230 3 A218 218 0 0 1 230 437 A210 210 0 0 0 230 17 Z" fill="#b5975a"/>
      <circle role="img" aria-label="Photo of hands installing a wiper blade on a car windshield" cx="214" cy="220" r="205" fill="url(#aboutPhoto)"/>
    </svg>
  </div>
  <div class="abs about-copy">
    <h2>ABOUT US</h2>
    <h3>NQB CLEARO SEE IT CLEARLY</h3>
    <p>There's much to see here. So, take your time, look around, and learn all there is to know about us. We hope you enjoy our site and take a moment to drop us a line.</p>
    <p>NQB Clearo is focused on safety and visibility, our wipers are the best possible solution to help you see while you are driving through heavy rain and snow conditions.</p>
    <p>We are now happy to announce that we are donating a set of NQB Clearo Wipers to school busses for every $100 spent this year. When you purchase from us, you are a part of helping bus drivers see clearly world wide.</p>
    <div class="btn" style="margin-top:22px">LEARN MORE <span class="arrow"><svg width="12" height="12" viewBox="0 0 12 12"><path d="M2 6h7M6 3l3 3-3 3" stroke="#b5975a" stroke-width="1.8" fill="none"/></svg></span></div>
  </div>

  <section class="abs products">
    <svg width="1200" height="776" viewBox="0 0 1200 776">
      <defs><linearGradient id="prodBg" x1="0" y1="0" x2="0" y2="1"><stop offset="0" stop-color="#1c1c1c"/><stop offset="1" stop-color="#262626"/></linearGradient></defs>
      <path d="M0 22 L40 18 L70 26 L110 14 L150 24 L200 12 L240 22 L290 16 L330 26 L380 10 L430 22 L470 16 L520 24 L560 14 L610 22 L660 12 L700 24 L750 16 L790 26 L840 12 L890 22 L930 18 L980 26 L1020 12 L1070 22 L1110 16 L1160 24 L1200 14 V776 H0 Z" fill="url(#prodBg)"/>
    </svg>
  </section>
  <div class="abs products-head">
    <h2>OUR <span class="gold">PRODUCTS</span></h2>
    <p>Silicone wiper blades are better than rubber in many aspects of wipe performance.</p>
  </div>
  <div class="abs carousel-arrow" style="left:50px;top:1744px">‹</div>
  <div class="abs carousel-arrow" style="left:1128px;top:1744px">›</div>
  <div class="abs product" style="left:112px;top:1628px">
    <div class="product-photo" role="img" aria-label="Photo of a wiper blade in front of a sign"><div class="quick-view">Quick View</div></div>
    <div class="product-name">NQB CLEARO</div><div class="product-size">24 inches</div><div class="product-price">$15.00</div><div class="stars">★★★★<span class="off">★</span></div>
  </div>
  <div class="abs product" style="left:362px;top:1628px">
    <div class="product-photo" role="img" aria-label="Photo of a wiper blade in front of a sign"></div>
    <div class="product-name">NQB CLEARO</div><div class="product-size">18 inches</div><div class="product-price">$14.00</div><div class="stars">★★★★★</div>
  </div>
  <div class="abs product" style="left:613px;top:1628px">
    <div class="product-photo" role="img" aria-label="Photo of a wiper blade in front of a sign"></div>
    <div class="product-name">NQB CLEARO</div><div class="product-size">14 inches</div><div class="product-price">$14.00</div><div class="stars">★★★★★</div>
  </div>
  <div class="abs product" style="left:863px;top:1628px">
    <div class="product-photo" role="img" aria-label="Photo of a wiper blade in front of a sign"></div>
    <div class="product-name">NQB CLEARO</div><div class="product-size">16 inches</div><div class="product-price">$14.00</div><div class="stars">★★★★★</div>
  </div>

  <div class="abs fact" style="left:100px;top:2229px">
    <h4>Did you know?</h4>
    <p>Normal wiper blades should be replaced every six to twelve months? Here at NQB Clearo our wipers are designed to hug the curvature of every windshield. We use the beam blade design to provide the best visibility during the rain and snow.</p>
  </div>
  <div class="abs fact highlight" style="left:441px;top:2229px">
    <h4>Silicone or rubber?</h4>
    <p>Silicone is more durable than rubber. Silicone wipers can last twice as long as rubber. NQB Clearo wipers use a special type of silicone that will not only outlast, but also outperform the competition. It's also designed to have better resistance to the elements and can withstand the hot summers and coldest of winters.</p>
  </div>
  <div class="abs fact" style="left:783px;top:2229px">
    <h4>Is it time to replace?</h4>
    <p>If you are experiencing any of these problems, then it is time to replace. We cover rain and snow with these windshield wipers. NQB Clearo offers the perfect size blade that is made to specifically fit your vehicle.</p>
  </div>
  <div class="abs fact-icon" style="left:208px;top:2174px">
    <svg width="50" height="50" viewBox="0 0 50 50" fill="none" stroke="#161616" stroke-width="3"><circle cx="25" cy="25" r="20"/><path d="M25 22v13M25 15v2"/></svg>
  </div>
  <div class="abs fact-icon" style="left:548px;top:2174px">
    <svg width="54" height="54" viewBox="0 0 54 54" fill="none" stroke="#161616"><ellipse cx="27" cy="27" rx="22" ry="18" stroke-width="6"/><ellipse cx="27" cy="25" rx="12" ry="8" stroke-width="3"/></svg>
  </div>
  <div class="abs fact-icon" style="left:890px;top:2174px">
    <svg width="50" height="50" viewBox="0 0 50 50" fill="none" stroke="#161616" stroke-width="3"><rect x="6" y="6" width="14" height="14" rx="2"/><rect x="30" y="30" width="14" height="14" rx="2"/><path d="M26 12h12v10M34 18l4 4 4-4M24 38H12V28M8 32l4-4 4 4"/></svg>
  </div>

  <div class="abs signup-bg"></div>
  <section class="abs signup">
    <h2>SIGN UP FOR A DISCOUNT</h2>
    <div class="divider"></div>
    <p>Get 10% off your first purchase when you sign up for our yearly reminder.</p>
    <div class="signup-form"><span>hello@nqbclearo.com</span><b>SIGNUP</b></div>
  </section>

  <div class="abs brand footer-brand">
    <span class="brand-dot"></span>
    <span class="brand-name">NQB Clearo</span>
  </div>
  <div class="abs footer-card" style="left:187px;top:3024px">
    <div class="footer-icon"><svg width="30" height="30" viewBox="0 0 22 22"><path d="M6 4c1-1 2 0 2.5 1.2l.8 1.8c.3.7-.4 1.3-.9 1.8.8 1.8 2 3 3.8 3.8.5-.5 1.1-1.2 1.8-.9l1.8.8C17 13 18 14 17 15c-2.2 2.2-6 0-8.3-2.2S3.8 6.2 6 4z" fill="#fff"/></svg></div>
    <h5>Phone Number</h5><p>(123) 456-7890</p>
  </div>
  <div class="abs footer-card" style="left:467px;top:3024px">
    <div class="footer-icon"><svg width="30" height="30" viewBox="0 0 30 30"><rect x="4" y="8" width="22" height="15" rx="1.5" fill="#fff"/><path d="M4 9l11 8 11-8" stroke="#b5975a" stroke-width="1.8" fill="none"/></svg></div>
    <h5>Email Address</h5><p>info@nqbclearo.com</p>
  </div>
  <div class="abs footer-card" style="left:748px;top:3024px">
    <div class="footer-icon"><svg width="30" height="30" viewBox="0 0 30 30"><path d="M15 3a9 9 0 019 9c0 7-9 15-9 15S6 19 6 12a9 9 0 019-9z" fill="#fff"/><circle cx="15" cy="12" r="3.5" fill="#b5975a"/></svg></div>
    <h5>Address</h5><p>P.O. Box 12345, lorem,<br>Ipsum 89511</p>
  </div>

  <div class="abs footer-bar"></div>
  <div class="abs footer-social"><span></span><span></span><span></span></div>
  <nav class="abs footer-links"><span>Home</span><span>About Us</span><span>Product</span><span>Contact us</span></nav>
  <div class="abs footer-copy">©2023 NQBclearo.com see it clearly &nbsp;|&nbsp; Disclaimer, Terms &amp; Conditions</div>

</main>
</body>
</html>
```